Travel Company is looking for a STAND OUT Business Card

I need a unique Business Card that will truly stand out. Nothing too busy. Simple is good, right? Not looking for a standard design either. No cookie cutter layout. We are a Travel Company that works more with Companies than Travelers. I had an idea to focus and emphasis on the 2 logo a bit more. This is not necessary, however thought it would look interesting. I am just looking for something interesting and a bit different. Does't have to completely off the wall crazy, just not your run of the mill business card.

Target Market(s)

Hoteliers, Resort Management, Call Centers, Executives, Travelers, Families, Businesses

Industry/Entity Type

Hospitality

Contact Information for Business Card

President/CEO - Marcus T Bellamy (title not necessary if design doesn't allow for it)
contact - (407) 555-0186
email - mbellamy@wayfarenow.example
address - 4812 Quillmore Ave #164
Orlando, FL 32804
website - www.wayfarenow.example

Font styles to use
Serif
Other font styles liked:
• Avenir Next LT Pro BOLD

Requirements
Must have
• simple look and design. Unique design
Nice to have
• I attached the 2 logo separate from the main logo. This can be used separately from the Main Logo, together with the main logo or as main logo. I included the logo font. Use it or not, designers choice.
Should not have
• cookie cutter design. Little use of red other than the logo

```html
<!DOCTYPE html>
<html lang="en">
<head>
<meta charset="utf-8">
<title>Wayfarenow – Round Business Card</title>
<link href="https://fonts.googleapis.com/css2?family=Libre+Baskerville&family=Source+Sans+3:wght@400;700;800&display=swap" rel="stylesheet">
<style>
  :root {
    --backdrop: #1f1f1f;
    --card: #f4f4f4;
    --ink: #2a2a2a;
    --ink-soft: #4a4a4a;
    --accent: #e8333d;
    --accent-muted: #d98a86;
  }
  * { box-sizing: border-box; margin: 0; padding: 0; }
  html, body {
    width: 1200px; height: 886px; overflow: hidden;
    background: var(--backdrop);
  }
  .canvas { position: relative; width: 1200px; height: 886px; }

  .card {
    position: absolute;
    width: 440px; height: 440px;
    border-radius: 50%;
    background: var(--card);
  }
  .card--front { left: 110px; top: 150px; display: flex; align-items: center; justify-content: center; }
  .card--back { left: 650px; top: 300px; }

  .brand-name {
    font-family: "Source Sans 3", sans-serif;
    font-weight: 800;
    font-size: 64px;
    letter-spacing: -1px;
    color: var(--ink);
    display: flex; align-items: center; gap: 14px;
  }
  .brand-dot {
    width: 22px; height: 22px; border-radius: 50%;
    background: var(--accent);
  }

  .identity {
    position: absolute; left: 82px; top: 128px;
    border-left: 6px solid var(--accent);
    padding-left: 12px;
  }
  .identity__name {
    font-family: "Libre Baskerville", serif;
    font-size: 27px; color: var(--ink); line-height: 1.1;
  }
  .identity__title {
    font-family: "Libre Baskerville", serif;
    font-size: 17px; color: var(--accent); line-height: 1.3;
  }

  .contact {
    position: absolute; left: 100px; top: 218px;
    list-style: none;
    font-family: "Source Sans 3", sans-serif;
    font-size: 17px; color: var(--ink-soft); line-height: 1.3;
  }
  .contact__item { display: flex; align-items: flex-start; gap: 10px; margin-bottom: 8px; }
  .contact__icon { width: 16px; height: 16px; flex: none; margin-top: 3px; fill: var(--accent); }
  .contact__icon--web { fill: none; stroke: var(--accent-muted); stroke-width: 1.6; }
</style>
</head>
<body>
<main class="canvas">

  <section class="card card--front" aria-label="Card front">
    <p class="brand-name"><span class="brand-dot"></span>wayfarenow</p>
  </section>

  <section class="card card--back" aria-label="Card back">
    <div class="identity">
      <p class="identity__name">Marcus T Bellamy</p>
      <p class="identity__title">CEO</p>
    </div>
    <ul class="contact">
      <li class="contact__item">
        <svg class="contact__icon" viewBox="0 0 16 16"><path d="M3 2h3l1 4-2 1a8 8 0 0 0 4 4l1-2 4 1v3a2 2 0 0 1-2 2A12 12 0 0 1 1 4a2 2 0 0 1 2-2z"/></svg>
        <span>(407) 555-0186</span>
      </li>
      <li class="contact__item">
        <svg class="contact__icon" viewBox="0 0 16 16"><path d="M1 3h14v10H1z M1 3l7 6 7-6" stroke="#f4f4f4" stroke-width="1.2"/></svg>
        <span>mbellamy@wayfarenow.example</span>
      </li>
      <li class="contact__item">
        <svg class="contact__icon" viewBox="0 0 16 16"><path d="M8 1a5 5 0 0 1 5 5c0 4-5 9-5 9S3 10 3 6a5 5 0 0 1 5-5zm0 3a2 2 0 1 0 0 4 2 2 0 0 0 0-4z"/></svg>
        <span>4812 Quillmore Ave #164<br>Orlando, FL 32804</span>
      </li>
      <li class="contact__item">
        <svg class="contact__icon contact__icon--web" viewBox="0 0 16 16"><circle cx="8" cy="8" r="6.5"/><path d="M1.5 8h13M8 1.5c-3 3-3 10 0 13M8 1.5c3 3 3 10 0 13"/></svg>
        <span>www.wayfarenow.example</span>
      </li>
    </ul>
  </section>

</main>
</body>
</html>
```